Business Card Design for Photographer

Updating business card design. Must use included logo. We're a luxury wedding photography business. Elegancy, luxury, consistency are messages we wish to convey.

Visit our website at www.colvanderose.com to familiarize yourself more with our brand design currently (fonts, colors etc.). This is what we want to maintain.

Target Market(s)

Luxury Brides and Grooms

Industry/Entity Type

Wedding

Contact Information for Business Card

Current logo (attached to brief)
Name: Colin Vanderose
Phone: 5871302948
website/blog
Email

Requirements
Must have
• Current logo (attached to brief)
• Name: Colin Vanderose
• Phone: 5871302948
• website/blog
• Email
• Instagram username
Should not have
• bright colors, fonts that don't suit our brand (visit www.colvanderose.com)

```html
<!DOCTYPE html>
<html lang="en">
<head>
<meta charset="utf-8">
<title>Colin Vanderose Photographers – Business Card</title>
<link rel="stylesheet" href="https://fonts.googleapis.com/css2?family=Josefin+Sans:wght@300;400&family=Yellowtail&display=swap">
<style>
  :root {
    --backdrop: #e9e9e9;
    --card: #f2f2f2;
    --ink: #707070;
    --ink-soft: #9a9a9a;
    --mark: #8a8a8a;
    --shadow: rgba(0,0,0,0.12);
  }
  * { margin: 0; padding: 0; box-sizing: border-box; }
  html, body {
    width: 1200px; height: 1000px; overflow: hidden;
    background: var(--backdrop);
  }
  .sheet {
    width: 1200px; height: 1000px;
    display: flex; flex-direction: column; align-items: center; justify-content: center;
    gap: 60px;
  }
  .card {
    position: relative;
    width: 700px; height: 400px;
    background: var(--card);
    box-shadow: 0 6px 22px var(--shadow);
  }

  /* Front */
  .brand {
    position: absolute; left: 0; right: 0; top: 130px;
    display: flex; flex-direction: column; align-items: center;
    font-family: "Josefin Sans", sans-serif; font-weight: 400; color: var(--ink);
  }
  .brand-mark {
    width: 48px; height: 40px; background: var(--mark); margin-bottom: 18px;
  }
  .brand-name {
    font-size: 22px; letter-spacing: 5px; text-transform: uppercase;
  }
  .brand-tagline {
    font-size: 11px; letter-spacing: 7px; text-transform: uppercase; margin-top: 6px;
  }
  .front-web {
    position: absolute; right: 60px; bottom: 40px;
    font-family: "Yellowtail", cursive; font-size: 20px; color: var(--ink);
  }

  /* Back */
  .contact {
    position: absolute; left: 150px; top: 120px;
    font-family: "Josefin Sans", sans-serif; font-weight: 300; color: var(--ink-soft);
  }
  .contact-name {
    display: flex; align-items: center; gap: 10px;
    font-weight: 400; font-size: 24px; letter-spacing: 3px; text-transform: uppercase;
    color: var(--ink); margin-bottom: 14px;
  }
  .contact-name .name-mark { width: 26px; height: 22px; background: var(--mark); }
  .contact-line {
    display: flex; align-items: center; gap: 14px;
    font-size: 23px; letter-spacing: 1.5px; margin-bottom: 12px;
  }
  .contact-icon { width: 26px; height: 26px; flex: none; }
  .contact-icon rect { fill: var(--mark); }
  .contact-icon path { fill: none; stroke: var(--card); stroke-width: 1.6; stroke-linejoin: round; stroke-linecap: round; }
</style>
</head>
<body>
<main class="sheet">
  <section class="card card-front">
    <div class="brand">
      <div class="brand-mark"></div>
      <div class="brand-name">Colin Vanderose</div>
      <div class="brand-tagline">Photographers</div>
    </div>
    <div class="front-web">www.colvanderose.com</div>
  </section>

  <section class="card card-back">
    <div class="contact">
      <div class="contact-name"><span class="name-mark"></span>Colin Vanderose</div>
      <div class="contact-line">
        <svg class="contact-icon" viewBox="0 0 26 26" aria-hidden="true">
          <rect width="26" height="26" rx="5"/>
          <path d="M8 7 L11 7 L12 11 L10 12.5 Q12 16 14 17 L15.5 15 L19 16 L19 19 Q12 20 7 11 Z"/>
        </svg>
        <span>5871302948</span>
      </div>
      <div class="contact-line">
        <svg class="contact-icon" viewBox="0 0 26 26" aria-hidden="true">
          <rect width="26" height="26" rx="5"/>
          <path d="M6 8 H20 V18 H6 Z M6 8 L13 14 L20 8"/>
        </svg>
        <span>colin@colvanderose.com</span>
      </div>
      <div class="contact-line">
        <svg class="contact-icon" viewBox="0 0 26 26" aria-hidden="true">
          <rect width="26" height="26" rx="5"/>
        </svg>
        <span>colvanderosephoto</span>
      </div>
    </div>
  </section>
</main>
</body>
</html>
```